We need a redesign of our current 8 page A4 double sided brochure

We're Looking for a Talented Designer to Revamp Our Brochure
Bright Paths HUB is seeking a creative and experienced designer to help us redesign our brochure. We’re looking to create a minimalist, cleaner look that stands out and perfectly aligns with our brand guidelines. With the copy already in place, we just need your expertise to bring our vision to life.
What we need:
A fresh, modern design that aligns with our brand and messaging.
A minimalist aesthetic that clearly communicates our value.
Experience working with brand guidelines and existing content.
Attention to detail and an eye for creating impactful, visually appealing layouts.
If you’re passionate about design and ready to collaborate with a growing company, we’d love to hear from you! Reach out to us today to discuss how you can help us make a lasting impression with our new brochure. Please note we are not using the logo with the children it it any more and would like to stick to the blue, grey white and pink, and ensure that the power of white really stands out in this brochure. The copy in this brochure is not the final copy. There is a style guide with our colours and fonts
Updates
Hi I have just uploaded our Copy right images that I would like used instead of the stock photos if you could please change the stock photos out to use ours. Many thanks

```html
<!DOCTYPE html>
<html lang="en">
<head>
<meta charset="utf-8">
<title>Bright Paths HUB – Flyer</title>
<link href="https://fonts.googleapis.com/css2?family=Montserrat:ital,wght@0,400;0,500;0,700;1,400&display=swap" rel="stylesheet">
<style>
  :root {
    --navy: #21386a;
    --accent: #ee7fae;
    --sky: #30b3e7;
    --paper: #ffffff;
    --ink-soft: #4f4f55;
    --photo-dark: #6b6c6e;
    --photo-light: #8a8b8d;
  }
  * { margin: 0; padding: 0; box-sizing: border-box; }
  html, body { width: 855px; height: 1200px; overflow: hidden; background: var(--paper); }
  body { font-family: "Montserrat", Arial, sans-serif; color: var(--navy); }
  .flyer { position: relative; width: 855px; height: 1200px; background: var(--paper); overflow: hidden; }

  .hero-art { position: absolute; left: 0; top: 0; width: 855px; height: 677px; display: block; }

  .brand-name {
    position: absolute; left: 0; width: 855px; top: 574px;
    text-align: center; font-weight: 700; font-size: 36px; line-height: 1; color: var(--sky);
    white-space: nowrap;
  }

  .headline {
    position: absolute; left: 0; width: 855px; top: 680px;
    text-align: center; font-weight: 700; font-size: 82px; line-height: 1;
    letter-spacing: 0.01em; white-space: nowrap;
  }
  .subline {
    position: absolute; left: 0; width: 855px; top: 770px;
    text-align: center; font-weight: 400; font-style: italic; font-size: 47px; line-height: 1;
    white-space: nowrap;
  }

  .service-tag { position: absolute; left: 213px; top: 847px; width: 401px; height: 64px; }
  .service-tag svg { position: absolute; inset: 0; width: 100%; height: 100%; }
  .service-tag span {
    position: absolute; inset: 0; display: flex; align-items: center; justify-content: center;
    font-weight: 500; font-size: 33px; line-height: 1; letter-spacing: 0.28em; padding-left: 0.28em;
    color: var(--navy); white-space: nowrap;
  }

  .features { position: absolute; left: 22px; top: 936px; width: 796px; display: flex; }
  .feature { flex: 1; text-align: center; }
  .feature-icon { width: 60px; height: 64px; display: block; margin: 0 auto; }
  .feature-title {
    margin-top: 10px; font-weight: 500; font-size: 21px; letter-spacing: 0.12em; line-height: 1;
    white-space: nowrap;
  }
  .feature-text { margin-top: 4px; font-size: 14.5px; line-height: 18px; color: var(--ink-soft); white-space: nowrap; }

  .contact-bar { position: absolute; left: 22px; top: 1083px; width: 796px; height: 66px; display: flex; }
  .contact-phone {
    width: 491px; background: var(--navy); color: var(--paper);
    display: flex; align-items: center; padding-left: 28px; gap: 6px; white-space: nowrap;
  }
  .contact-label { font-size: 17px; letter-spacing: 0.16em; font-weight: 500; }
  .contact-number { font-size: 34px; font-weight: 400; letter-spacing: 0.01em; }
  .contact-web {
    flex: 1; background: var(--accent); color: var(--navy);
    display: flex; align-items: center; justify-content: center;
    font-size: 17px; letter-spacing: 0.14em; font-weight: 400; white-space: nowrap;
  }
</style>
</head>
<body>
<main class="flyer">

  <svg class="hero-art" viewBox="0 0 1654 1320" preserveAspectRatio="none">
    <defs>
      <linearGradient id="photoTone" x1="0" y1="0" x2="0" y2="1">
        <stop offset="0" stop-color="#6b6c6e"/>
        <stop offset="1" stop-color="#8a8b8d"/>
      </linearGradient>
      <clipPath id="frameClip"><rect x="42" y="42" width="1540" height="1278"/></clipPath>
      <filter id="softShadow" x="-5%" y="-5%" width="110%" height="120%">
        <feDropShadow dx="0" dy="6" stdDeviation="6" flood-color="#000" flood-opacity="0.28"/>
      </filter>
    </defs>
    <rect class="hero-photo" x="42" y="42" width="1540" height="1000" fill="url(#photoTone)"
          role="img" aria-label="Photo of three young schoolgirls in white blouses, grey vest and navy blazer uniforms, standing against a grey studio backdrop"/>
    <g clip-path="url(#frameClip)">
      <path class="wave-navy" fill="var(--navy)"
        d="M42 1320 V1000 C300 960 520 860 800 830 C1050 805 1150 950 1300 980 C1420 1000 1500 1000 1582 985 V1320 Z"/>
      <path class="wave-accent" fill="var(--accent)" filter="url(#softShadow)"
        d="M42 1320 V1110 C350 1100 500 950 650 890 C750 850 880 850 960 880 C1100 940 1200 1080 1582 1095 V1320 Z"/>
      <path class="wave-white" fill="var(--paper)" filter="url(#softShadow)"
        d="M42 1320 V1290 C350 1280 500 1100 620 980 C720 880 900 860 1000 920 C1150 1010 1250 1280 1582 1290 V1320 Z"/>
      <ellipse class="accent-disc" cx="268" cy="878" rx="238" ry="282"
        fill="var(--navy)" stroke="var(--paper)" stroke-width="22"/>
    </g>
  </svg>

  <div class="brand-name">Bright Paths HUB</div>

  <h1 class="headline">LOREM IPSUM</h1>
  <p class="subline">LOREM IPSUM</p>

  <div class="service-tag">
    <svg viewBox="0 0 401 64" preserveAspectRatio="none" aria-hidden="true">
      <polygon points="12,0 389,0 401,32 389,64 12,64 0,32" fill="var(--accent)"/>
    </svg>
    <span>OUR SERVICE</span>
  </div>

  <section class="features">
    <div class="feature">
      <svg class="feature-icon" viewBox="0 0 60 64" aria-hidden="true">
        <rect x="4" y="8" width="52" height="52" rx="7" fill="none" stroke="var(--accent)" stroke-width="6"/>
        <line x1="18" y1="2" x2="18" y2="14" stroke="var(--accent)" stroke-width="6" stroke-linecap="round"/>
        <line x1="42" y1="2" x2="42" y2="14" stroke="var(--accent)" stroke-width="6" stroke-linecap="round"/>
        <line x1="4" y1="20" x2="56" y2="20" stroke="var(--accent)" stroke-width="4"/>
        <text x="30" y="48" text-anchor="middle" font-family="Montserrat, sans-serif" font-weight="700" font-size="22" fill="var(--accent)">25</text>
      </svg>
      <h2 class="feature-title">LOREM IPSUM</h2>
      <p class="feature-text">Lorem ipsum dolor sit amet,<br>consectetur adipiscing elit.</p>
    </div>
    <div class="feature">
      <svg class="feature-icon" viewBox="0 0 60 64" aria-hidden="true">
        <path d="M10 60 V10 a8 8 0 0 1 8 -8 h24 a8 8 0 0 1 8 8 V60" fill="none" stroke="var(--accent)" stroke-width="6"/>
        <line x1="2" y1="60" x2="58" y2="60" stroke="var(--accent)" stroke-width="5" stroke-linecap="round"/>
        <g fill="var(--accent)">
          <rect x="18" y="14" width="10" height="9"/><rect x="32" y="14" width="10" height="9"/>
          <rect x="18" y="27" width="10" height="9"/><rect x="32" y="27" width="10" height="9"/>
          <rect x="18" y="40" width="10" height="9"/><rect x="32" y="40" width="10" height="9"/>
        </g>
      </svg>
      <h2 class="feature-title">LOREM IPSUM</h2>
      <p class="feature-text">Lorem ipsum dolor sit amet,<br>consectetur adipiscing elit.</p>
    </div>
    <div class="feature">
      <svg class="feature-icon" viewBox="0 0 60 64" aria-hidden="true">
        <circle cx="30" cy="24" r="20" fill="none" stroke="var(--accent)" stroke-width="6"/>
        <circle cx="30" cy="24" r="6" fill="var(--accent)"/>
        <line x1="30" y1="44" x2="30" y2="60" stroke="var(--accent)" stroke-width="6" stroke-linecap="round"/>
      </svg>
      <h2 class="feature-title">LOREM IPSUM</h2>
      <p class="feature-text">Lorem ipsum dolor sit amet,<br>consectetur adipiscing elit.</p>
    </div>
  </section>

  <footer class="contact-bar">
    <div class="contact-phone">
      <span class="contact-label">GET IN TOUCH :</span>
      <span class="contact-number">+123 - 234 - 555</span>
    </div>
    <div class="contact-web">WWW.YOURCOMPANY.COM</div>
  </footer>

</main>
</body>
</html>
```